Rw building ventures pty ltd

This is a development and construction company. Website can be set up on our domain rwbuildworks.net if we could change the domain to rwbuildworks.com.au would be great

Want the page to have eye catching designs, red, black and white are the preffered colours.

Check out www.toluqin.com.au it is my former company with my partner which i am now venturing out on my own, that is the perfect example of the website i want even allot of the information would be the same

Industry/Entity Type

Construction

Coding

Coded - Design and coding required

Number of Pages Required

5+ page

Requirements
Must have
• Company logo eye catching designs

```html
<!DOCTYPE html>
<html lang="en">
<head>
<meta charset="utf-8">
<title>About Us – RW Buildworks</title>
<link href="https://fonts.googleapis.com/css2?family=Montserrat:wght@400;500;600;700&display=swap" rel="stylesheet">
<style>
:root{
  --red:#e8391d;
  --ink:#111111;
  --text:#2a2a2a;
  --muted:#4a4a4a;
  --line:#dcdcdc;
  --soft:#f6f7f9;
  --white:#ffffff;
  --black:#000000;
}
*{box-sizing:border-box;margin:0;padding:0}
html,body{width:1200px;height:3022px;overflow:hidden}
body{font-family:'Montserrat',sans-serif;color:var(--text);background:var(--white);position:relative}
.abs{position:absolute}
/* header */
.site-header{position:absolute;left:0;top:0;width:1200px;height:106px;background:var(--white)}
.brand{position:absolute;left:161px;top:34px;display:flex;align-items:center;gap:12px}
.brand-mark{width:26px;height:26px;background:var(--red)}
.brand-name{font-size:26px;font-weight:600;letter-spacing:2px;color:var(--ink);text-transform:uppercase}
.main-nav{position:absolute;right:163px;top:44px;display:flex;gap:21px;font-size:14px;font-weight:500;text-transform:uppercase}
.main-nav a{color:var(--ink);text-decoration:none}
.main-nav a.active{color:var(--red)}
/* media placeholders */
.photo{position:absolute}
.hero{left:0;top:106px;width:1200px;height:298px;background:linear-gradient(90deg,#8d877c,#cfc9bd 35%,#6f6a62 60%,#d8d3ca 85%,#a39a8a)}
.about-photo{left:161px;top:560px;width:407px;height:374px;border-top:6px solid #2c3440;background:linear-gradient(160deg,#3a6fd0 0%,#8aa8dc 35%,#7d7f84 60%,#4d4f53 100%)}
.room-photo{left:161px;top:1179px;width:877px;height:390px;background:linear-gradient(180deg,#e6e0d3 0%,#c9b89a 40%,#8a7256 75%,#6a5540 100%)}
.expert-photo{left:633px;top:1755px;width:405px;height:380px;background:linear-gradient(135deg,#8e949c 0%,#c4cbd2 40%,#e98a2b 70%,#e9e6df 100%)}
/* breadcrumb */
.breadcrumb{left:163px;top:426px;font-size:14px;font-weight:500;text-transform:uppercase;color:var(--ink)}
.breadcrumb .sep{margin:0 8px}
.breadcrumb .current{color:var(--red)}
.section-title{position:absolute;left:0;width:1200px;text-align:center;font-size:30px;font-weight:700;letter-spacing:1px;color:var(--ink);text-transform:uppercase}
.copy{font-size:13.2px;line-height:24.5px;color:var(--text)}
.copy p+p{margin-top:10px}
.about-copy{left:628px;top:558px;width:414px}
.about-wide{left:180px;top:962px;width:840px;text-align:center}
.tagline{left:0;top:1048px;width:1200px;text-align:center;font-size:20px;font-weight:700;line-height:31px;color:var(--red);letter-spacing:.3px}
.experts-sub{left:0;top:1692px;width:1200px;text-align:center;font-size:13.5px;color:var(--text)}
.expert{left:163px;top:1760px;width:420px}
.expert h3{font-size:22px;font-weight:700;color:var(--ink);text-transform:uppercase;letter-spacing:.5px}
.expert .role{font-size:15px;color:var(--red);margin-top:4px;margin-bottom:10px}
/* contact */
.contact{position:absolute;left:0;top:2215px;width:1200px;height:542px;background:var(--soft)}
.field{position:absolute;background:var(--white);border:1px solid var(--line);font-size:12px;color:var(--text);padding:0 14px;display:flex;align-items:center}
.field.area{align-items:flex-start;padding-top:14px}
.caret{position:absolute;right:14px;top:50%;margin-top:-2px;width:0;height:0;border-left:4px solid transparent;border-right:4px solid transparent;border-top:5px solid var(--ink)}
.send-btn{position:absolute;left:510px;top:422px;width:180px;height:45px;background:var(--red);color:var(--white);font-size:15px;font-weight:600;letter-spacing:.5px;display:flex;align-items:center;justify-content:center;text-transform:uppercase}
/* footer */
.site-footer{position:absolute;left:0;top:2757px;width:1200px;height:265px;background:var(--black);color:var(--white)}
.footer-brand{position:absolute;left:161px;top:101px;display:flex;align-items:center;gap:10px}
.footer-brand .brand-mark{width:22px;height:22px;background:var(--white)}
.footer-brand .brand-name{color:var(--white);font-size:21px}
.contact-chip{position:absolute;top:91px;height:45px;display:flex;overflow:hidden}
.chip-icon{flex:0 0 44px;height:45px;background:var(--red);display:flex;align-items:center;justify-content:center}
.chip-text{flex:1;background:var(--white);color:var(--ink);font-size:13px;display:flex;align-items:center;justify-content:center;height:45px;white-space:nowrap}
.social{position:absolute;top:91px;width:44px;height:45px;background:var(--red);display:flex;align-items:center;justify-content:center}
.footer-rule{position:absolute;left:161px;top:186px;width:878px;height:1px;background:#5a5a5a}
.footer-nav{position:absolute;left:164px;top:216px;display:flex;gap:27px;font-size:14px}
.copyright{position:absolute;right:163px;top:216px;font-size:14px}
</style>
</head>
<body>
<header class="site-header">
  <div class="brand"><span class="brand-mark"></span><span class="brand-name">RW Buildworks</span></div>
  <nav class="main-nav">
    <a href="#">Home</a><a href="#" class="active">About Us</a><a href="#">Services</a><a href="#">Projects</a><a href="#">Contact Us</a>
  </nav>
</header>

<div class="photo hero" role="img" aria-label="Modern living room interior with television wall, dining area and sofa"></div>

<div class="abs breadcrumb">Home<span class="sep">/</span><span class="current">About Us</span></div>

<h1 class="section-title" style="top:480px">About Us</h1>

<div class="photo about-photo" role="img" aria-label="Modern two-storey house with grey cladding and glass balcony"></div>

<div class="abs copy about-copy">
  <p>Lorem ipsum dolor sit amet, consectetuer adipiscing el sed diam nonummy nibh euismod tincidunt ut let dolore magna aliquam erat volutpat.</p>
  <p>Ut wisi enim ad minim veniam, quis ud exerci in ullamcorper suscipit lobortis nisl ut aliquip ex ea commodo coquat. Duis autem vel eum iriure dolor in hendrerit in vulputte velit esse molestie consequat, vel illum dolore eu feugat nulla facilisis at vero eros et accumsan et iusto odio dignissim qui blandit praesent luptatum zzril delenit.</p>
  <p>Lorem ipsum dolor sit amet, consectetuer adipiscing el sed diam nonummy nibh euismod tincidunt ut let dolore magna aliquam erat volutpat.Ut wisi enim ad minim veniam quis ud exerci in ullamcorper suscipit lobortis nisl.</p>
</div>

<div class="abs copy about-wide">Ut wisi enim ad minim veniam, quis ud exerci in ullamcorper suscipit lobortis nisl ut aliquip ex ea commodo coquat. Duis autem vel eum iriure dolor in hendrerit in vulputte velit esse molestie consequat, vel illum dolore eu feugat nulla facilisis at vero eros et accumsan et iusto odio dignissim qui blandit praesent luptatum zzril delenit.</div>

<div class="abs tagline">After All Our Vision Quality, Innovation And Excellence;<br>You Can Be Confident You’re In Good Hands At RW Buildworks.</div>

<div class="photo room-photo" role="img" aria-label="Luxury hotel-style bedroom with large bed, curtains and balcony doors"></div>

<h2 class="section-title" style="top:1640px">Your Experts</h2>
<p class="abs experts-sub">Meet your team of building and construction experts to take care of your project from beginning to completion.</p>

<div class="abs expert">
  <h3>Expert Name</h3>
  <p class="role">Managing Director</p>
  <div class="copy">
    <p>Lorem ipsum dolor sit amet, consectetuer adipiscing el sed diam nonummy nibh euismod tincidunt ut let dolore magna aliquam erat volutpat.</p>
    <p>Ut wisi enim ad minim veniam, quis ud exerci in ullamcorper suscipit lobortis nisl ut aliquip ex ea commodo coquat. Duis autem vel eum iriure dolor in hendrerit in vulputte velit esse molestie consequat, vel illum dolore eu feugat nulla facilisis at vero eros et accumsan et iusto odio dignissim qui blandit praesent luptatum zzril delenit.</p>
    <p>Lorem ipsum dolor sit amet, consectetuer adipiscing el sed diam nonummy nibh euismod tincidunt ut let.</p>
  </div>
</div>

<div class="photo expert-photo" role="img" aria-label="Two construction workers in hard hats and safety vests reviewing plans on site"></div>

<section class="contact">
  <h2 class="section-title" style="top:70px">Contact Us</h2>
  <div class="field" style="left:318px;top:137px;width:274px;height:45px">Name</div>
  <div class="field" style="left:608px;top:137px;width:274px;height:45px">Email</div>
  <div class="field" style="left:318px;top:195px;width:274px;height:45px">Phone</div>
  <div class="field" style="left:608px;top:195px;width:274px;height:45px">Inquiry for<span class="caret"></span></div>
  <div class="field area" style="left:318px;top:253px;width:564px;height:145px">Message here....</div>
  <div class="send-btn">Send a Message</div>
</section>

<footer class="site-footer">
  <div class="footer-brand"><span class="brand-mark"></span><span class="brand-name">RW Buildworks</span></div>
  <div class="contact-chip" style="left:412px;width:200px">
    <span class="chip-icon"><svg width="22" height="22" viewBox="0 0 24 24" fill="none" stroke="#fff" stroke-width="1.6"><path d="M5 3h4l2 5-2.5 1.5a11 11 0 0 0 6 6L16 13l5 2v4a2 2 0 0 1-2 2A17 17 0 0 1 3 5a2 2 0 0 1 2-2z"/></svg></span>
    <span class="chip-text">+61 (02) 5550 - 147</span>
  </div>
  <div class="contact-chip" style="left:622px;width:268px">
    <span class="chip-icon"><svg width="22" height="22" viewBox="0 0 24 24" fill="none" stroke="#fff" stroke-width="1.6"><rect x="3" y="5" width="18" height="14"/><path d="M3 5l9 8 9-8"/></svg></span>
    <span class="chip-text">info@rwbuildworks.com.au</span>
  </div>
  <span class="social" style="left:900px" role="img" aria-label="Professional profile"><svg width="20" height="20" viewBox="0 0 24 24" fill="none" stroke="#fff" stroke-width="1.6"><circle cx="12" cy="8" r="4"/><path d="M4 21c0-4.4 3.6-7 8-7s8 2.6 8 7"/></svg></span>
  <span class="social" style="left:947px" role="img" aria-label="Share page"><svg width="20" height="20" viewBox="0 0 24 24" fill="none" stroke="#fff" stroke-width="1.6"><circle cx="6" cy="12" r="2.5"/><circle cx="18" cy="6" r="2.5"/><circle cx="18" cy="18" r="2.5"/><path d="M8.2 10.8l7.6-3.6M8.2 13.2l7.6 3.6"/></svg></span>
  <span class="social" style="left:994px" role="img" aria-label="Send a message"><svg width="20" height="20" viewBox="0 0 24 24" fill="none" stroke="#fff" stroke-width="1.6"><path d="M4 5h16v11H9l-5 4z"/></svg></span>
  <div class="footer-rule"></div>
  <nav class="footer-nav"><span>Home</span><span>About Us</span><span>Services</span><span>Projects</span><span>Contact Us</span></nav>
  <div class="copyright">Copyright © 2022 RW Buildworks | All Rights Reserved</div>
</footer>
</body>
</html>
```